Printed Promo Flyer for new pet business

We need a double sided flyer design as per the given example flyer, just better looking and more fun.Flyers will need to be printed.Flyer size approx 10.5cm x 15cm. The text will need to be amended slightly afterwards to be more fun unless you can create a new tone of voice as well (should sound fun like breezy do it) Look and Feel: emotional, fun, loving, professional
See attached files.

Target Market(s)

Pet owners in the UK who want the convenience of getting their pets parasite treatment delivered to their door without the need of having to run to the vet or store for purchase

Industry/Entity Type

Pet Care

Colors
00a990
6b449b

Requirements
Must have
• all the content context as given in the example flyer.
Nice to have
• Tone of voice can be changed to be more fun (using Breezy as a guide)

```html
<!DOCTYPE html>
<html lang="en">
<head>
<meta charset="utf-8">
<title>Pet Guard Box – Promo Flyer</title>
<link href="https://fonts.googleapis.com/css2?family=Fjalla+One&family=Lilita+One&family=Luckiest+Guy&family=Patrick+Hand&family=Oswald:wght@500&family=Montserrat:wght@500&display=swap" rel="stylesheet">
<style>
:root{
  --board:#2c2c2c;
  --label:#c9c9c9;
  --teal:#00a990;
  --teal-soft:#7fcfd4;
  --purple:#6b449b;
  --purple-deep:#4a2a74;
  --yellow:#e9a912;
  --green-dark:#0f3b33;
  --red:#d8232a;
  --ink:#2a2a2a;
  --white:#ffffff;
}
*{margin:0;padding:0;box-sizing:border-box}
html,body{width:1200px;height:904px;overflow:hidden;background:var(--board)}
.board{position:relative;width:1200px;height:904px}
.side-label{position:absolute;top:26px;font:500 22px "Montserrat",sans-serif;color:var(--label);width:510px;text-align:center}
.caption{position:absolute;top:848px;left:0;width:1200px;text-align:center;font:500 24px "Montserrat",sans-serif;color:var(--label)}
.flyer{position:absolute;top:78px;width:510px;height:726px;overflow:hidden;background:radial-gradient(circle at 50% 40%,#fff 0%,#f3f3f5 70%,#e9e9ee 100%);box-shadow:0 8px 18px rgba(0,0,0,.45)}
.front{left:64px}
.back{left:629px}

/* front */
.brand-name{position:absolute;font-family:"Oswald",sans-serif;font-weight:500;white-space:nowrap;line-height:1}
.front .brand-name{left:42px;top:100px;font-size:36px;color:var(--purple);letter-spacing:1px}
.hero-photo{position:absolute;left:24px;top:24px;width:486px;height:520px;background:radial-gradient(ellipse at 52% 55%,#e2b98a 0%,#f0d6b4 35%,rgba(255,255,255,0) 70%)}
.front-wave{position:absolute;left:0;top:490px;width:510px;height:236px}
.offer-panel{position:absolute;left:72px;top:452px;width:365px;height:190px}
.offer-top{position:absolute;left:86px;top:466px;font:25px/32px "Fjalla One",sans-serif;color:var(--white);white-space:nowrap;transform:rotate(-1.5deg)}
.offer-top em{font-style:normal;color:#3fd0b3}
.offer-for{position:absolute;left:0;width:510px;top:506px;text-align:center;font:27px/32px "Luckiest Guy","Lilita One","Fjalla One",sans-serif;color:var(--red);-webkit-text-stroke:2px #fff;paint-order:stroke fill}
.offer-pet{position:absolute;left:0;width:510px;top:532px;text-align:center;font:100px/96px "Luckiest Guy","Lilita One","Fjalla One",sans-serif;color:var(--white);text-shadow:5px 5px 0 var(--purple)}
.offer-banner{position:absolute;left:84px;top:630px;width:316px;height:48px}
.offer-banner-text{position:absolute;left:84px;top:632px;width:316px;text-align:center;font:30px/42px "Fjalla One",sans-serif;color:var(--white);transform:rotate(1deg)}
.front-url{position:absolute;left:0;width:510px;top:688px;text-align:center;font:14px/20px "Fjalla One",sans-serif;letter-spacing:5px;color:var(--white)}

/* back */
.pill{position:absolute;left:131px;width:248px;height:42px;border-radius:21px;text-align:center;font:28px/42px "Fjalla One",sans-serif;color:var(--white);box-shadow:0 6px 8px rgba(0,0,0,.18)}
.pill.why{top:19px;background:var(--purple)}
.pill.how{top:365px;background:var(--yellow)}
.benefit-icon{position:absolute;left:49px;width:52px;height:52px}
.benefit-title{position:absolute;left:120px;font:20px/22px "Fjalla One",sans-serif;color:var(--teal);white-space:nowrap}
.benefit-title.alt{color:var(--purple)}
.benefit-text{position:absolute;left:120px;width:360px;font:16px/20px "Patrick Hand",cursive;color:var(--ink)}
.rule{position:absolute;left:100px;width:360px;height:1px;background:linear-gradient(90deg,var(--teal-soft),rgba(127,207,212,0))}
.steps{position:absolute;left:80px;top:425px;list-style:none}
.steps li{position:relative;padding-left:22px;height:27px;font:19px/26px "Patrick Hand",cursive;color:var(--ink);white-space:nowrap}
.steps li svg{position:absolute;left:0;top:5px}
.back-wave{position:absolute;left:0;top:604px;width:510px;height:122px}
.back .brand-name{left:24px;top:687px;font-size:14px;color:var(--teal);letter-spacing:.5px}
.back-url{position:absolute;left:147px;top:684px;font:15px/20px "Fjalla One",sans-serif;color:var(--white);letter-spacing:.5px;white-space:nowrap}
.price-badge{position:absolute;left:311px;top:542px;width:168px;height:168px}
.price-first{position:absolute;left:311px;width:168px;top:571px;text-align:center;font:22px/24px "Patrick Hand",cursive;color:var(--yellow);letter-spacing:1px}
.price-amount{position:absolute;left:311px;width:168px;top:590px;text-align:center;font:52px/58px "Fjalla One",sans-serif;color:var(--purple-deep)}
.price-code{position:absolute;left:311px;width:168px;top:646px;text-align:center;font:13px/16px "Fjalla One",sans-serif;color:var(--purple-deep)}
.price-code-value{position:absolute;left:311px;width:168px;top:667px;text-align:center;font:15px/20px "Fjalla One",sans-serif;color:var(--white);letter-spacing:4px}
</style>
</head>
<body>
<div class="board">
  <div class="side-label" style="left:64px">Front</div>
  <div class="side-label" style="left:629px">Back</div>

  <section class="flyer front">
    <div class="hero-photo" role="img" aria-label="Photo of a fluffy Pomeranian puppy sitting beside a ginger and white cat"></div>
    <div class="brand-name">PET GUARD BOX</div>
    <svg class="front-wave" viewBox="0 0 510 236" aria-hidden="true">
      <path d="M0 30 C40 0 80 50 130 28 S220 20 255 40 S360 10 420 30 S490 40 510 20 V236 H0Z" fill="var(--yellow)"/>
      <path d="M0 60 C40 30 90 80 140 55 S230 50 260 70 S370 40 420 58 S490 70 510 48 V236 H0Z" fill="var(--purple)"/>
    </svg>
    <svg class="offer-panel" viewBox="0 0 365 190" aria-hidden="true">
      <path d="M0 14 L365 0 L340 190 L30 190Z" fill="var(--green-dark)"/>
    </svg>
    <div class="offer-top">The Best <em>Protection and Care</em></div>
    <div class="offer-for">For Your</div>
    <div class="offer-pet">PET</div>
    <svg class="offer-banner" viewBox="0 0 316 48" aria-hidden="true">
      <path d="M6 0 L316 6 L310 48 L0 42Z" fill="var(--red)"/>
    </svg>
    <div class="offer-banner-text">WITH PET GUARD BOX</div>
    <div class="front-url">WWW.PETGUARDBOX.CO.UK</div>
  </section>

  <section class="flyer back">
    <div class="pill why">WHY PET GUARD BOX?</div>

    <svg class="benefit-icon" style="top:84px" viewBox="0 0 52 52" aria-hidden="true"><circle cx="26" cy="26" r="26" fill="var(--teal-soft)"/><ellipse cx="26" cy="28" rx="7" ry="9" fill="#fff"/><circle cx="26" cy="17" r="4" fill="#fff"/><path d="M19 24 L12 20 M19 30 L12 32 M33 24 L40 20 M33 30 L40 32 M22 36 L18 41 M30 36 L34 41" stroke="#fff" stroke-width="2.5" stroke-linecap="round"/></svg>
    <div class="benefit-title" style="top:77px">PRATECTION &amp; CARE</div>
    <div class="benefit-text" style="top:102px">Protection against all major parasites to avoid putting your pet and your family at risk.</div>
    <div class="rule" style="top:154px"></div>

    <svg class="benefit-icon" style="top:154px" viewBox="0 0 52 52" aria-hidden="true"><circle cx="26" cy="26" r="26" fill="var(--teal-soft)"/><circle cx="26" cy="26" r="13" fill="none" stroke="#fff" stroke-width="3"/><path d="M26 19 V26 H32" stroke="#fff" stroke-width="3" fill="none" stroke-linecap="round"/></svg>
    <div class="benefit-title alt" style="top:162px">IN TIME</div>
    <div class="benefit-text" style="top:186px">Never having to remember when to treat your pet</div>
    <div class="rule" style="top:218px"></div>

    <svg class="benefit-icon" style="top:218px" viewBox="0 0 52 52" aria-hidden="true"><circle cx="26" cy="26" r="26" fill="var(--teal-soft)"/><path d="M14 22 A13 13 0 0 1 37 18 M38 30 A13 13 0 0 1 15 34" stroke="#fff" stroke-width="3" fill="none"/><path d="M37 12 V19 H30 M15 40 V33 H22" stroke="#fff" stroke-width="3" fill="none"/><rect x="20" y="21" width="12" height="10" fill="#fff"/></svg>
    <div class="benefit-title" style="top:225px">CONVENIENT</div>
    <div class="benefit-text" style="top:249px">Delivered directly to your letter box</div>
    <div class="rule" style="top:282px"></div>

    <svg class="benefit-icon" style="top:285px" viewBox="0 0 52 52" aria-hidden="true"><circle cx="26" cy="26" r="26" fill="var(--teal-soft)"/><text x="26" y="37" text-anchor="middle" font-family="Oswald,sans-serif" font-size="30" fill="#fff">£</text></svg>
    <div class="benefit-title alt" style="top:290px">LOW COST</div>
    <div class="benefit-text" style="top:312px">Never having to remember when to treat your pet</div>

    <div class="pill how">HOW IT WORKS</div>
    <ul class="steps">
      <li><svg width="16" height="16" viewBox="0 0 16 16" aria-hidden="true"><circle cx="8" cy="8" r="7" fill="none" stroke="var(--yellow)" stroke-width="1.5"/><path d="M4.5 8 L7 10.5 L11.5 5.5" stroke="var(--yellow)" stroke-width="1.5" fill="none"/></svg>Select which pet the treatment is for</li>
      <li><svg width="16" height="16" viewBox="0 0 16 16" aria-hidden="true"><circle cx="8" cy="8" r="7" fill="none" stroke="var(--yellow)" stroke-width="1.5"/><path d="M4.5 8 L7 10.5 L11.5 5.5" stroke="var(--yellow)" stroke-width="1.5" fill="none"/></svg>Choose your treatment type</li>
      <li><svg width="16" height="16" viewBox="0 0 16 16" aria-hidden="true"><circle cx="8" cy="8" r="7" fill="none" stroke="var(--yellow)" stroke-width="1.5"/><path d="M4.5 8 L7 10.5 L11.5 5.5" stroke="var(--yellow)" stroke-width="1.5" fill="none"/></svg>Select your preferred brand</li>
      <li><svg width="16" height="16" viewBox="0 0 16 16" aria-hidden="true"><circle cx="8" cy="8" r="7" fill="none" stroke="var(--yellow)" stroke-width="1.5"/><path d="M4.5 8 L7 10.5 L11.5 5.5" stroke="var(--yellow)" stroke-width="1.5" fill="none"/></svg>Choose between 1, 3, 6 or 12 months treatment box</li>
    </ul>

    <svg class="back-wave" viewBox="0 0 510 122" aria-hidden="true">
      <path d="M0 10 Q10 2 20 10 T40 10 T60 10 T80 10 T100 10 T120 10 T140 10 T160 10 T180 10 T200 10 T220 10 T240 10 T260 10 T280 10 T300 10 T320 10 T340 10 T360 10 T380 10 T400 10 T420 10 T440 10 T460 10 T480 10 T500 10 T520 10 V122 H0Z" fill="var(--yellow)"/>
      <path d="M0 14 Q10 6 20 14 T40 14 T60 14 T80 14 T100 14 T120 14 T140 14 T160 14 T180 14 T200 14 T220 14 T240 14 T260 14 T280 14 T300 14 T320 14 T340 14 T360 14 T380 14 T400 14 T420 14 T440 14 T460 14 T480 14 T500 14 T520 14 V122 H0Z" fill="var(--purple)"/>
      <rect x="0" y="100" width="510" height="22" fill="var(--purple-deep)" opacity=".5"/>
    </svg>
    <div class="brand-name">PET GUARD BOX</div>
    <div class="back-url">WWW.PETGUARDBOX.CO.UK</div>

    <svg class="price-badge" viewBox="0 0 168 168" aria-hidden="true">
      <circle cx="84" cy="84" r="84" fill="var(--purple-deep)"/>
      <circle cx="84" cy="84" r="74" fill="#fff"/>
      <clipPath id="badge-inner"><circle cx="84" cy="84" r="74"/></clipPath>
      <rect x="0" y="124" width="168" height="22" fill="var(--purple-deep)" clip-path="url(#badge-inner)"/>
    </svg>
    <div class="price-first">FIRST BOX</div>
    <div class="price-amount">£5·99</div>
    <div class="price-code">USE CODE</div>
    <div class="price-code-value">XXX</div>
  </section>

  <div class="caption">PRINTED PROMO FLYER FOR NEW PET BUSINESS</div>
</div>
</body>
</html>
```